cold brew coffee bottle label "MOSS TIDE"

minimalist pastel coloured labels for cold brew coffee.
the name of the company is "MOSS TIDE".
would like the labels in multiple pastel colours: pink, blue, green, and yellow/beige.
prefer the use of the dubai font which can be downloaded from https://www.lorvatype.com/download
"MOSS TIDE" must be in a shiny gold.
"DUBAI" must be in a shiny gold.
attached are: the two types of bottles that will be used, some label examples that i have attempted to create, and some other cold brew bottle ideas i found on snapquilt. also i like the colors that are on the labels on the tin containers of coffee beans.
label should have area for bar code.
each label will have its colour correspond to the coffee origin, for example; green for Brazilian coffee, blue for Ethiopian coffee, pink for Mexican coffee. i would like the origin to be mentioned on the label as well.
the label should also have a "consume by:" section where the date can be stamped.
Updates

please provide landscape and portrait designs as it is not decided which will be used yet Added Monday, September 11, 2017

Industry/Entity Type

It Company

Font styles to use
Other font styles liked:
• Dubai font

Requirements
Must have
• portrait and landscape designs.
• Dubai fontarea for barcode.
• "consume by:" area

```html
<!DOCTYPE html>
<html lang="en">
<head>
<meta charset="utf-8">
<title>MOSS TIDE – Cold Brew Label</title>
<link rel="stylesheet" href="https://fonts.googleapis.com/css2?family=Saira+Extra+Condensed:wght@300;400;500&display=swap">
<style>
  :root {
    --label-pastel: #f1e4c8;
    --frame-line: #8a7250;
    --page-white: #ffffff;
    --brand-gold: #b8872f;
    --rule-gold: #c9a05a;
    --ink-brown: #4a2a1c;
    --barcode-field: #ffffff;
  }
  html, body {
    margin: 0;
    padding: 0;
    width: 1064px;
    height: 1200px;
    overflow: hidden;
    background: var(--page-white);
  }
  .label {
    position: relative;
    width: 1064px;
    height: 1200px;
    background: var(--page-white);
    font-family: "Saira Extra Condensed", "Arial Narrow", sans-serif;
  }
  .label__panel {
    position: absolute;
    left: 11px;
    top: 11px;
    right: 11px;
    bottom: 11px;
    background: var(--label-pastel);
    border: 1px solid var(--frame-line);
  }
  .consume-by {
    position: absolute;
    left: 48px;
    top: 48px;
    margin: 0;
    color: var(--ink-brown);
    font-size: 34px;
    font-weight: 400;
    letter-spacing: 1.5px;
    line-height: 1;
  }
  .consume-by__stamp {
    display: block;
    width: 260px;
    height: 56px;
    margin-top: 12px;
    border: 2px dashed var(--frame-line);
    box-sizing: border-box;
  }
  .barcode-area {
    position: absolute;
    right: 48px;
    top: 48px;
    width: 240px;
    height: 120px;
    background: var(--barcode-field);
    border: 1px solid var(--frame-line);
  }
  .brand-rule {
    position: absolute;
    left: 251px;
    width: 520px;
    height: 5px;
    background: var(--rule-gold);
  }
  .brand-rule--top    { top: 530px; }
  .brand-rule--bottom { top: 686px; }
  .brand-name {
    position: absolute;
    left: 0;
    right: 0;
    top: 548px;
    margin: 0;
    text-align: center;
    font-weight: 500;
    font-size: 136px;
    line-height: 1;
    letter-spacing: 3px;
    color: var(--brand-gold);
  }
  .line {
    position: absolute;
    left: 0;
    right: 0;
    margin: 0;
    text-align: center;
    color: var(--ink-brown);
    font-weight: 400;
    font-size: 46px;
    line-height: 1;
    letter-spacing: 2px;
    text-transform: uppercase;
  }
  .line--origin-type { top: 817px; }
  .line--brewed      { top: 880px; }
  .line--ready       { top: 1004px; }
  .line--roasted     { top: 1066px; }
  .line__city {
    font-size: 58px;
    font-weight: 300;
    color: var(--brand-gold);
    vertical-align: -3px;
  }
</style>
</head>
<body>
  <main class="label">
    <div class="label__panel">
      <p class="consume-by">CONSUME BY:<span class="consume-by__stamp"></span></p>
      <div class="barcode-area" aria-label="Barcode area"></div>
      <div class="brand-rule brand-rule--top"></div>
      <h1 class="brand-name">MOSS TIDE</h1>
      <div class="brand-rule brand-rule--bottom"></div>
      <p class="line line--origin-type">Single Origin Coffee</p>
      <p class="line line--brewed">Brewed in Dubai</p>
      <p class="line line--ready">Costa Rica Ready to Consume</p>
      <p class="line line--roasted">Roasted and Brewed in <span class="line__city">Dubai</span></p>
    </div>
  </main>
</body>
</html>
```